Email Campaign Design for PR Agency - urgent

We are urgently looking for a designer to pull together a design for an upcoming email campaign focused around Christmas PR.

quillvane.com is an online PR platform for companies in the interiors sector. we focus on promoting our clients high res product images to journalists who write for leading magazines, so our email designs need to reflect that we're design-led, innovative, modern, image-focused, fresh and friendly.

There will be 3 separate email campaigns, but all based around the same template with only small changes for each.

We plan to use a Postbadger drag and drop facility for the send, so each graphic section needs to be saved as separate jpeg or png files.

We're thinking a tile-style format will work best, to separate the individual messages within the 1 email. Required copy/sections are listed below in the images.
Updates

A quick note to advise that although it's a Christmas campaign, we want to keep the look very fresh, minimal and design-led. Keep in mind that all of our clients are shops in the interiors industry, so they expect quite on-trend, innovative, creative design with a personable feel. 

Please only insert photos/graphics that are quite contemporary and design-led. and please do not insert a lot of red & dark green - we want to keep the design light and use our standard Lime green, deep purple, very pale grey and bright aqua blue - but only sparingly if possible. 

The Sketch Harbor site themselves have a very fun, modern, clean look - something similar is ideal. 

Target Market(s)

Interiors & Gift stores

Industry/Entity Type

Campaign

Requirements
Must have
• Quill Vane logo

Quill Vane lime green accents

If other colours are used, they must be a very pale grey, dark purple or bright aqua (see images attached)

Must be fresh, clean, modern, design-led, friendly design. As there is a lot of copy, the design needs to look as minimal as possible, but still with a Christmas theme.

Copy to be used can be found in the attached images. Layout is a little flexible if you can think of a better way to showcase the key messages.

Should not have
• Must not have dated graphics

Must not look too busy

Must not look traditional/classic at all

```html
<!DOCTYPE html>
<html lang="en">
<head>
<meta charset="utf-8">
<title>Quill Vane – Christmas PR campaign email</title>
<link rel="stylesheet" href="https://fonts.googleapis.com/css2?family=Carlito:wght@400;700&family=Gochi+Hand&family=Schoolbell&display=swap">
<style>
  :root{
    --lime:#b5e655;
    --lime-deep:#9fd23e;
    --lime-text:#6aaa1e;
    --orchid:#eda9f5;
    --orchid-deep:#d98ce8;
    --lilac-text:#d98ce8;
    --ink:#222222;
    --slate:#555555;
    --button:#6f6f6f;
    --button-dark:#5a5a5a;
    --gold:#f4d33a;
    --alert:#c8161d;
    --frame:#d8d8d8;
    --paper:#ffffff;
    --placeholder-grey:#e9e9e9;
    --hand:"Gochi Hand", "Schoolbell", cursive;
    --school:"Schoolbell", "Gochi Hand", cursive;
    --body:"Carlito", "Calibri", Arial, sans-serif;
  }
  *{box-sizing:border-box;margin:0;padding:0}
  html,body{width:800px;height:1200px;overflow:hidden;background:var(--paper)}
  body{position:relative;font-family:var(--body);color:var(--ink)}
  .email-frame{position:absolute;left:26px;top:27px;width:741px;height:1144px;border:1px solid var(--frame)}

  /* hero */
  .hero{position:absolute;left:60px;top:60px;width:672px;height:219px;background:var(--lime);border-radius:10px}
  .hero-tree{position:absolute;left:28px;top:5px;width:164px;height:207px;background:linear-gradient(160deg,#c6ee78,#a3d845);border-radius:8px}
  .brand-tag{position:absolute;right:0;top:20px;width:118px;height:37px;background:var(--paper);display:flex;align-items:center;justify-content:center;font-family:var(--body);font-size:14px;color:var(--slate);letter-spacing:1px}
  .hero-title{position:absolute;left:174px;top:62px;font-family:var(--hand);font-size:38px;color:var(--paper);text-shadow:0 0 6px rgba(255,255,255,.9),0 1px 2px rgba(90,130,20,.6);transform:rotate(1.5deg)}
  .hero-sub{position:absolute;left:260px;top:115px;font-family:var(--hand);font-size:28px;color:var(--ink)}
  .hero-fees{position:absolute;left:290px;top:157px;font-family:var(--hand);font-size:34px;color:var(--lime-text)}

  .intro{position:absolute;left:80px;top:298px;width:628px;font-size:16px;line-height:22px;color:var(--ink)}
  .intro .drop{font-size:24px;color:var(--lime-deep)}

  /* offer */
  .offer{position:absolute;left:60px;top:391px;width:672px;height:220px;background:var(--orchid);border-radius:10px;overflow:hidden}
  .offer-wave{position:absolute;left:0;bottom:0;width:672px;height:90px}
  .offer-head{position:absolute;left:112px;top:17px;font-size:17px;color:var(--ink)}
  .offer-gift{position:absolute;left:-15px;top:49px;width:178px;height:160px;background:linear-gradient(180deg,#fbeefd,#f3d3f8);border-radius:4px}
  .offer-copy{position:absolute;left:205px;top:62px;font-size:16px;line-height:20px}
  .offer-price{position:absolute;left:205px;top:101px;font-family:var(--school);font-size:25px;font-weight:700}
  .offer-month{position:absolute;left:205px;top:138px;font-size:23px}
  .offer-valid{position:absolute;left:176px;top:171px;font-size:13px}
  .cta{position:absolute;left:386px;top:67px;width:241px;height:90px;border-radius:10px;background:linear-gradient(180deg,var(--button),var(--button-dark));box-shadow:2px 3px 4px rgba(0,0,0,.3);text-align:center;color:var(--paper);text-decoration:none}
  .cta-lead{display:block;font-family:var(--hand);font-size:30px;color:var(--gold);margin-top:6px;line-height:32px}
  .cta-text{display:block;font-size:15px;line-height:21px;margin-top:2px}

  /* features */
  .stopwatch{position:absolute;left:168px;top:655px;width:74px;height:86px;background:var(--placeholder-grey);border-radius:50%}
  .miss-title{position:absolute;left:88px;top:752px;font-family:var(--hand);font-size:42px;color:var(--lilac-text)}
  .miss-text{position:absolute;left:82px;top:803px;font-size:16px}
  .showcase-word{position:absolute;left:456px;top:828px;transform:rotate(-90deg);transform-origin:0 0;font-family:var(--hand);font-size:40px;line-height:40px;color:var(--lime-text)}
  .magazine{position:absolute;left:515px;top:643px;width:160px;height:108px;background:linear-gradient(160deg,#f0f0f0,#dcdcdc);border-radius:4px}
  .showcase-text{position:absolute;left:508px;top:772px;width:205px;font-size:16px;line-height:21px}

  /* clients */
  .clients-title{position:absolute;left:55px;top:866px;font-family:var(--school);font-size:22px;color:var(--slate)}
  .clients-rule{position:absolute;left:36px;top:866px;width:450px;height:40px}
  .client-list{position:absolute;left:118px;top:916px;display:flex;gap:14px;list-style:none}
  .client{height:28px;padding:0 8px;display:flex;align-items:center;font-size:14px;font-weight:700;color:var(--slate);background:#f2f2f2}

  /* footer */
  .question{position:absolute;left:52px;top:976px;font-family:var(--school);font-size:33px;color:var(--alert);letter-spacing:1px}
  .contact{position:absolute;left:52px;top:1016px;font-size:16px}
  .contact strong{font-weight:700}
  .sign-off{position:absolute;left:53px;top:1042px;font-family:var(--school);font-size:22px;color:var(--slate)}
  .merry{position:absolute;left:50px;top:1074px;font-family:var(--hand);font-size:60px;color:var(--lilac-text)}
  .bird-branch{position:absolute;left:553px;top:1005px;width:212px;height:86px;background:linear-gradient(180deg,#f7f3f0,#ebe3dc);border-radius:6px}
  .small-gift{position:absolute;left:580px;top:1098px;width:44px;height:50px;background:#c9434a;border-radius:2px}
  .footer-brand{position:absolute;left:458px;top:1131px;font-size:14px;letter-spacing:1px;color:var(--slate)}
  .team{position:absolute;left:636px;top:1129px;font-size:15px;color:#888}
</style>
</head>
<body>
<div class="email-frame"></div>

<section class="hero">
  <div class="hero-tree" role="img" aria-label="Illustration of a minimal swirled Christmas tree with a star on top"></div>
  <div class="brand-tag">Quill Vane</div>
  <h1 class="hero-title">Christmas PR is under way!</h1>
  <p class="hero-sub">Sign Up Now to Receive</p>
  <p class="hero-fees">Membership Fees</p>
</section>

<p class="intro"><span class="drop">W</span>ith monthly magazines bringing out Christmas gift guides and decoration stories as early as October, NOW is the time to focus on securing key press coverage for your products for the biggest time of the year.</p>

<section class="offer">
  <svg class="offer-wave" viewBox="0 0 672 90" preserveAspectRatio="none" aria-hidden="true">
    <path d="M0 40 C160 10 420 10 672 45 L672 90 L0 90 Z" fill="var(--orchid-deep)"/>
  </svg>
  <p class="offer-head">Receive our Premium membrship for the price of the Essential package.</p>
  <div class="offer-gift" role="img" aria-label="Sketched illustration of a gift box tied with a bow"></div>
  <p class="offer-copy">That’s all of our<br>PR services for</p>
  <p class="offer-price">Just $300</p>
  <p class="offer-month">per Month!</p>
  <p class="offer-valid">Offer Valid until Friday 19th July only</p>
  <a class="cta" href="#offer">
    <span class="cta-lead">Click here</span>
    <span class="cta-text">to read more &amp;<br>activate your old image</span>
  </a>
</section>

<div class="stopwatch" role="img" aria-label="Sketched illustration of a ringing stopwatch"></div>
<p class="miss-title">Don’t Miss Out!</p>
<p class="miss-text">on key&nbsp; Chirstmas Coverage this&nbsp; year</p>

<p class="showcase-word">Showcase</p>
<div class="magazine" role="img" aria-label="Sketched illustration of open magazine pages"></div>
<p class="showcase-text">your products to over 1000 journalists from home &amp; lifestyle magazines</p>

<p class="clients-title">Some of the companies using Quill Vane</p>
<svg class="clients-rule" viewBox="0 0 450 40" aria-hidden="true">
  <path d="M0 36 C120 26 300 24 410 28" fill="none" stroke="var(--alert)" stroke-width="1.5"/>
  <path d="M420 12 C430 16 438 22 438 30 M430 28 L438 32 L442 24" fill="none" stroke="var(--alert)" stroke-width="1.5"/>
</svg>
<ul class="client-list">
  <li class="client">Lanefield</li>
  <li class="client">Fairleaf Store</li>
  <li class="client">Mandarine</li>
  <li class="client">Ovalo</li>
  <li class="client">Farside Living</li>
</ul>

<p class="question">Question?</p>
<p class="contact"><strong>Contact us</strong> anytime on 02 5550 4127 or info@quillvane.com.au</p>
<p class="sign-off">We look forward to hearing from you!</p>
<p class="merry">Merry Cristmas</p>

<div class="bird-branch" role="img" aria-label="Illustration of a small bird in a Santa hat on a bare branch"></div>
<div class="small-gift" role="img" aria-label="Illustration of a small red patterned gift box"></div>
<p class="footer-brand">Quill Vane</p>
<p class="team">Australia team</p>
</body>
</html>
```